Product Photographer in Jacksonville Florida need marketing post card

need postcard to mail and hand deliver to prospects. Goal is to get more product photography jobs into studio. I shoot jewelry, food, wine, art, products, clothes, etc. Include my logo, phone, email, Black font, white background, clean, cool, modern,...i like the fint that Tallowmere Quill mag uses on cover

Target Market(s)

artist that design & create jewlery, painting, pottery, Restaurants food photos,

Industry/Entity Type

Jewelry

Font styles to use
Serif

Colors
ffffff

Requirements
Must have
• I like font like Lumen Magazine title, Tallowmere Quill mag title
• 1-3 cool product images. maybe jewlery, food, clothes
• cool, clean, modern, edgy ...not corporate feel.
• white back ground, black text
• image is everything
Nice to have
• clean lots of white space ok.
Should not have
• no bright colors,

```html
<!DOCTYPE html>
<html lang="en">
<head>
<meta charset="utf-8">
<title>Marlo Kent Photography — Postcard</title>
<link href="https://fonts.googleapis.com/css2?family=Bodoni+Moda:ital,opsz,wght@0,6..96,400;1,6..96,400&display=swap" rel="stylesheet">
<style>
  :root {
    --page: #ffffff;
    --ink: #0b0b0b;
    --sky-light: #f4fbfd;
    --sky-mid: #d3ecf3;
    --surface: #b9dbe4;
    --surface-deep: #8fbfcc;
    --glass-light: #e6f5f8;
    --glass-mid: #c2e3eb;
    --glass-deep: #7fb3c4;
    --label-blue: #3a4d8a;
  }
  * { margin: 0; padding: 0; box-sizing: border-box; }
  html, body {
    width: 1200px;
    height: 1000px;
    overflow: hidden;
    background: var(--page);
  }
  .postcard {
    position: relative;
    width: 1200px;
    height: 1000px;
    background: var(--page);
    font-family: "Bodoni Moda", "Didot", serif;
    font-optical-sizing: none;
    font-variation-settings: "opsz" 96;
    font-weight: 400;
    color: var(--ink);
  }
  .backdrop {
    position: absolute;
    left: 57px;
    top: 102px;
    width: 1101px;
    height: 734px;
    background:
      radial-gradient(ellipse 40% 50% at 22% 45%, var(--sky-light) 0%, rgba(244,251,253,0) 70%),
      linear-gradient(180deg, var(--sky-mid) 0%, var(--sky-light) 55%, var(--sky-mid) 79%, var(--surface) 79.5%, var(--surface-deep) 100%);
  }
  .product-photo {
    position: absolute;
    left: 612px;
    top: 128px;
    width: 430px;
    height: 708px;
    border-radius: 30px 30px 0 0;
    background:
      linear-gradient(180deg, rgba(127,179,196,0) 50%, rgba(58,77,138,0.35) 52%, rgba(58,77,138,0.35) 68%, rgba(127,179,196,0) 70%),
      linear-gradient(90deg, var(--glass-mid) 0%, var(--glass-light) 30%, var(--glass-mid) 50%, var(--glass-light) 75%, var(--glass-deep) 100%);
  }
  .masthead {
    position: absolute;
    left: 150px;
    top: 180px;
    width: 440px;
    text-align: center;
    font-weight: 400;
  }
  .masthead__name {
    display: block;
    font-size: 15px;
    letter-spacing: 2px;
    line-height: 1;
    margin-left: 128px;
    text-align: left;
  }
  .masthead__title {
    display: block;
    font-size: 78px;
    line-height: 1;
    margin-top: -10px;
    letter-spacing: -1px;
  }
  .services {
    position: absolute;
    left: 200px;
    top: 287px;
    width: 400px;
    list-style: none;
    text-align: center;
    font-style: italic;
    font-size: 60px;
    line-height: 77px;
  }
  .studio-mark {
    position: absolute;
    left: 350px;
    top: 702px;
    width: 115px;
    text-align: center;
    line-height: 1.15;
  }
  .studio-mark__tagline {
    display: block;
    font-size: 5px;
    letter-spacing: 0.5px;
    margin-bottom: 6px;
  }
  .studio-mark__square {
    display: block;
    width: 48px;
    height: 48px;
    margin: 0 auto 8px;
    background: var(--ink);
  }
  .studio-mark__name {
    display: block;
    font-size: 12px;
    letter-spacing: 1px;
  }
  .studio-mark__sub {
    display: block;
    font-size: 8px;
    letter-spacing: 2.5px;
    border-bottom: 1px solid var(--ink);
    padding-bottom: 2px;
  }
</style>
</head>
<body>
  <main class="postcard">
    <div class="backdrop"></div>
    <div class="product-photo" role="img" aria-label="Product photograph: three clear glass soda bottles with labels standing on a reflective surface against a pale blue backdrop"></div>

    <h1 class="masthead">
      <span class="masthead__name">MARLO KENT</span>
      <span class="masthead__title">Photography</span>
    </h1>

    <ul class="services">
      <li>jewlery</li>
      <li>painting</li>
      <li>pottery</li>
      <li>restaurants</li>
      <li>food photos</li>
    </ul>

    <div class="studio-mark">
      <span class="studio-mark__tagline">architectural • wedding • portrait</span>
      <span class="studio-mark__square"></span>
      <span class="studio-mark__name">MARLO KENT</span>
      <span class="studio-mark__sub">PHOTOGRAPHY</span>
    </div>
  </main>
</body>
</html>
```